Vetern Mailer for Mortgage Refinance

Hello, I need some options in my KR mailers we send out here in the USA! A sample of our mailer has been included. I need all the verbiage the same. The data merge points need to stay on too. Please make this pop. We have a high end TELM printer and a Z auto folding machine. Letter goes into a number 10 envelope with windows. So lets see what you can do. One with colors below is our company colors and then one black, white, gray.
Blue - 3399FF------ R 51 G 153 B 255
Orange - FF9933----- R 255 G 153 B 51
Black – 333333------ R 51 G 51 B 51
White – FFFFFF------ R 255 G 255 B 255

Target Market(s)

United States Military Service Members

Industry/Entity Type

Mortgage Lender

Requirements
Must have
• Margins for folding with Z and Number 10 Envelope with two windows

```html
<!DOCTYPE html>
<html lang="en">
<head>
<meta charset="utf-8">
<title>KR Refinance Mailer – Front and Back</title>
<link href="https://fonts.googleapis.com/css2?family=Montserrat:ital,wght@0,400;0,500;0,600;0,700;0,800;1,400;1,500&display=swap" rel="stylesheet">
<style>
:root{
  --blue:#3399ff;
  --orange:#ff9933;
  --ink:#333333;
  --white:#ffffff;
  --stage:#d9dadc;
  --panel:#e3e7ee;
  --muted:#6b6f76;
}
*{box-sizing:border-box;margin:0;padding:0}
html,body{width:1200px;height:2428px;overflow:hidden}
body{background:var(--stage);font-family:"Montserrat",sans-serif;color:var(--ink);position:relative}
.page{position:absolute;left:140px;width:920px;height:1190px;background:var(--white);box-shadow:0 4px 18px rgba(0,0,0,.12);overflow:hidden}
.page--front{top:16px}
.page--back{top:1222px}
.abs{position:absolute}

/* merge fields */
.field{position:absolute;height:20px;border:1.5px solid var(--orange);border-radius:10px;font-size:9px;font-weight:600;line-height:17px;color:var(--ink);white-space:nowrap;overflow:hidden}
.field__tag{display:inline-block;background:var(--orange);color:var(--white);border-radius:10px;padding:0 10px;height:17px}

/* address panel */
.disclaim-top{left:50px;top:100px;width:380px;font-size:14px;line-height:19px;color:var(--muted)}
.recipient{left:50px;top:186px;font-size:24px;font-weight:700}
.recipient span{color:var(--blue)}
.recipient-addr{left:50px;top:222px;font-size:14px;font-weight:500;display:flex;align-items:center;gap:6px}
.offer-box{left:540px;top:40px;width:340px;height:200px;background:var(--blue);border-radius:14px;box-shadow:0 6px 14px rgba(51,153,255,.3)}
.offer-pill{position:absolute;left:20px;width:300px;height:30px;background:var(--white);border-radius:15px;font-size:14px;text-align:center;line-height:30px;color:var(--ink)}
.offer-amount{position:absolute;left:0;right:0;top:104px;text-align:center;color:var(--white);font-size:76px;font-weight:800;line-height:80px}
.offer-amount sup{font-size:34px;vertical-align:28px}
.defer{left:540px;top:256px;width:340px;text-align:center;font-size:12px;line-height:16px}
.tollfree{left:540px;top:292px;width:340px;text-align:center;color:var(--orange);font-size:22px;font-weight:700}
.phone{left:540px;top:318px;width:340px;display:flex;justify-content:center;align-items:center;gap:8px;font-size:38px;font-weight:700}
.hours{left:540px;top:368px;width:340px;text-align:center;font-size:16px;font-weight:500}
.hours b{color:var(--orange);font-weight:600}

/* letter panel */
.letter-band{left:0;top:425px;width:920px;height:400px;background:linear-gradient(90deg,#f7f7f8 0%,#ececee 100%)}
.salutation{left:50px;top:468px;font-size:17px;font-weight:700}
.letter-body{left:50px;top:500px;width:470px;font-size:14px;line-height:20px}
.escrow{left:50px;top:730px;width:420px;font-size:19px;font-weight:600;color:var(--orange);line-height:25px}
.hero-photo{left:540px;top:460px;width:350px;height:320px;border-radius:8px;background:radial-gradient(ellipse at 55% 45%,#b5523a 0%,#8d4a3d 35%,#c9a25a 65%,rgba(236,236,238,0) 80%)}

/* benefits panel */
.benefit-band{left:0;top:825px;width:920px;height:365px;background:var(--panel)}
.benefit-card{position:absolute;left:40px;width:425px;border:2px solid var(--blue);border-radius:12px;background:var(--white)}
.benefit-card__title{position:absolute;left:-2px;top:-2px;background:var(--blue);color:var(--white);font-size:14px;font-weight:600;padding:5px 18px 5px 14px;border-radius:12px 0 14px 0}
.benefit-list{position:absolute;left:14px;right:10px;top:40px;display:grid;grid-template-columns:1fr 1fr;column-gap:16px;row-gap:8px;list-style:none;font-size:11px;line-height:14px}
.benefit-list li{position:relative;padding-left:13px}
.benefit-list li::before{content:"";position:absolute;left:0;top:4px;width:6px;height:6px;border-radius:50%;background:var(--orange)}
.recommend{left:500px;top:850px;width:385px;font-size:13px;font-style:italic;line-height:18px}
.brand{left:500px;top:982px;width:185px;font-size:18px;font-weight:600;letter-spacing:2px;color:var(--blue);white-space:nowrap}
.cashout{left:700px;top:968px;width:220px;height:54px;background:var(--orange);color:var(--white);border-radius:4px 0 0 4px;padding:6px 14px;white-space:nowrap}
.cashout small{display:block;font-size:9px;font-weight:600;line-height:12px}
.cashout strong{font-size:22px;font-weight:700;line-height:28px}
.cashout em{font-size:10px;font-style:normal}
.company{left:700px;top:1034px;display:flex;gap:6px}
.company__name{color:var(--blue);font-size:15px;font-weight:700;line-height:17px}
.company__addr{font-size:12px;line-height:16px;margin-top:4px}
.nmls-tag{display:inline-block;background:var(--blue);color:var(--white);border-radius:10px;padding:0 10px;height:17px}
.reverse-note{left:40px;top:1165px;font-size:10px;font-style:italic;letter-spacing:1px}

/* back page */
.back-lead{left:50px;top:470px;width:820px;font-size:11px;font-weight:600;line-height:14px;color:var(--blue)}
.terms-box{left:50px;top:520px;width:820px;background:var(--orange);color:var(--white);border-radius:10px;padding:12px 16px;font-size:8.5px;line-height:12px}
.terms-box h3{font-size:10px;font-weight:700;margin-bottom:4px}
.fine{position:absolute;left:50px;width:820px;font-size:8.5px;line-height:12px;color:var(--ink)}
.fine h4{color:var(--blue);font-size:9.5px;font-weight:700;margin-bottom:2px}
ol.fine{list-style:none}
ol.fine li{margin-bottom:8px}
ol.fine li h4::before{content:attr(data-n);display:inline-block;width:13px;height:13px;border-radius:50%;background:var(--blue);color:var(--white);text-align:center;font-size:8px;line-height:13px;margin-right:4px}
.desk-photo{left:0;top:920px;width:920px;height:270px;background:linear-gradient(180deg,rgba(255,255,255,0) 0%,#e6e4e0 30%,#cfc9c0 100%)}
</style>
</head>
<body>

<section class="page page--front" aria-label="Mailer front">
  <div class="field" style="left:50px;top:40px;width:380px"><span class="field__tag">RE</span></div>
  <div class="field" style="left:50px;top:66px;width:380px"><span class="field__tag">Loan ID Number</span></div>
  <p class="abs disclaim-top">Summit Crest Home Loans LLC is not affiliated with your current lender nor is it an agency of the Federal Government.</p>
  <p class="abs recipient">Daniel <span>Carter</span></p>
  <p class="abs recipient-addr"><svg width="14" height="18" viewBox="0 0 14 18"><path d="M7 0a7 7 0 0 0-7 7c0 5 7 11 7 11s7-6 7-11a7 7 0 0 0-7-7z" fill="#3399ff"/><circle cx="7" cy="7" r="2.6" fill="#fff"/></svg>2345 Lorem ipsum city 242</p>
  <div class="field" style="left:50px;top:262px;width:380px"><span class="field__tag">City</span></div>
  <div class="field" style="left:50px;top:288px;width:380px"><span class="field__tag">State</span></div>
  <div class="field" style="left:50px;top:314px;width:380px"><span class="field__tag">Zip</span></div>

  <div class="abs offer-box">
    <div class="offer-pill" style="top:18px">Close_month</div>
    <div class="offer-pill" style="top:58px">Skip_month</div>
    <div class="offer-amount"><sup>$</sup>0</div>
  </div>
  <p class="abs defer">You may be able to defer<br>your next two payments.¹</p>
  <p class="abs tollfree">Call Toll Free</p>
  <p class="abs phone"><svg width="26" height="26" viewBox="0 0 26 26"><circle cx="13" cy="13" r="13" fill="#3399ff"/><path d="M9 7c1 0 2 3 2 3l-1.3 1.4c.8 1.8 2.2 3.2 4 4L15 14s3 1 3 2-1.5 3-3 3C11 19 7 15 7 11c0-1.5 1-4 2-4z" fill="#fff"/></svg>555 0142 7730</p>
  <p class="abs hours">Weekdays &nbsp;| &nbsp;<b>6 a.m - 5 p.m</b> PST</p>

  <div class="abs letter-band"></div>
  <p class="abs salutation">Dear Daniel,</p>
  <p class="abs letter-body">We are contacting you regarding your &lt;&lt;balance&gt;&gt; KR loan. Our review has indicated that because of homes appreciating in &lt;&lt;city&gt;&gt;, you may now qualify for additional benefits. These benefits may include lowering your monthly mortgage payment, deferring up to two payments, refund of escrow, and $35,000 or more cash-out.¹ Call our KR Program Specialist at &lt;&lt; phone_number&gt;&gt; at your earliest convenience to receive a detailed explanation of how you may be able to access these benefits.²</p>
  <p class="abs escrow">You may also receive a check back from your escrow account.²</p>
  <div class="abs hero-photo" role="img" aria-label="Photo of a model brick house beside stacks of gold coins"></div>

  <div class="abs benefit-band"></div>
  <div class="benefit-card" style="top:845px;height:155px">
    <span class="benefit-card__title">Additional Benefits Include</span>
    <ul class="benefit-list">
      <li>100% LTV Cash-Out Available</li>
      <li>No out-of-pocket appraisal deposit</li>
      <li>Pay off High Interest Debt</li>
      <li>No Private Mortgage Insurance</li>
      <li>Complete a long overdue home renovation</li>
    </ul>
  </div>
  <div class="benefit-card" style="top:1015px;height:142px">
    <span class="benefit-card__title">KR IRRRL Benefits</span>
    <ul class="benefit-list">
      <li>Reduce Your Current Interest Rate</li>
      <li>Fast Closings in 8-14 days</li>
      <li>Mortgage-Only Credit Report</li>
      <li>No Income or Asset Verification Required</li>
      <li>No Appraisal Required</li>
    </ul>
  </div>
  <p class="abs recommend">We recommend you call our office at &lt;&lt;phone_number&gt;&gt; within the next 3-5 business days as market rates fluctuate. By taking action now your next mortgage payment may not be due until &lt;&lt;next_pay_month&gt;&gt;.² To avoid further delay, please call today.</p>
  <p class="abs brand">SUMMIT CREST</p>
  <div class="abs cashout"><small>CASH OUT OPTIONS</small><strong>$35,000</strong> <em>Or More</em></div>
  <div class="field" style="left:500px;top:1034px;width:180px"><span class="field__tag">Phone</span></div>
  <div class="field" style="left:500px;top:1060px;width:180px"><span class="field__tag">Loan ID Number</span></div>
  <div class="field" style="left:500px;top:1086px;width:180px;border-color:var(--blue);color:var(--blue)"><span class="nmls-tag">NMLS</span>&nbsp; 0000000 00000</div>
  <div class="abs company">
    <svg width="14" height="18" viewBox="0 0 14 18" style="margin-top:2px"><path d="M7 0a7 7 0 0 0-7 7c0 5 7 11 7 11s7-6 7-11a7 7 0 0 0-7-7z" fill="#ff9933"/><circle cx="7" cy="7" r="2.6" fill="#fff"/></svg>
    <div><p class="company__name">Summit Crest Home<br>Loans LLC</p><p class="company__addr">N Harbor Rd Ste 410<br>Mesa, AZ 85201</p></div>
  </div>
  <p class="abs reverse-note">*Please see reverse for disclaimer</p>
</section>

<section class="page page--back" aria-label="Mailer back">
  <p class="abs back-lead">Offer is available only for loans made or arranged through Summit Crest Home Loans LLC, NMLS 0000000, N Harbor Rd Ste 410, Mesa, AZ 85201, who is not associated with, or acting on behalf of your current lender or any government agency. Verification of employment may apply. This program is exclusive to the beneficiary named above and is nontransferable.</p>
  <div class="abs terms-box">
    <h3>TERMS &amp; CONDITIONS</h3>
    <p>You are receiving this notice because you appear to satisfy certain credit criteria derived from information held by a consumer reporting agency. This offer may not be extended if, after you respond, you no longer meet those criteria. The final terms depend on verification of income, assets, property value and title. Rates and payments shown are estimates only and may change without notice. If you do not wish to receive future offers of this type, you may contact the consumer reporting agencies to opt out. Your request will be honored as required under applicable federal law.</p>
  </div>
  <div class="fine" style="top:640px">
    <h4>STATE DISCLOSURE REQUIREMENTS</h4>
    <p>Summit Crest Home Loans LLC is a licensed mortgage lender. Licensing details for each state in which we operate are available on request and through the national registry. Loans are offered subject to state law, underwriting approval and availability. Not all products are available in all areas, and program guidelines may be revised at any time without prior notice to the recipient.</p>
  </div>
  <ol class="fine" style="top:720px">
    <li><h4 data-n="1">Deferred mortgage payments</h4><p>You may not make your mortgage payment for the month that you are closing your new loan. Deferred interest is added to the new balance and repaid over the loan term. Review your closing figures carefully.</p></li>
    <li><h4 data-n="2">Escrow Account Refund (if applicable)</h4><p>Any refund from your escrow account is governed by your current servicer and its timelines. Please contact your servicer for details about your account balance and refund status.</p></li>
    <li><h4 data-n="3">Example cash-out of $35,000</h4><p>Cash-out amount depends on available equity, credit profile and appraised value. Call 555-014-7730 for a personalized estimate.</p></li>
    <li><h4 data-n="4">Your circumstances may vary</h4><p>Equal Housing Lender. We do not discriminate on any basis prohibited by law.</p></li>
  </ol>
  <div class="abs desk-photo" role="img" aria-label="Photo of a desk with a calculator, a jar of coins, a small wooden house model and a hand"></div>
</section>

</body>
</html>
```